Australian Grown Coffee needs a premium, OUTSTANDING!! Coffee bag design

Morrell coffee is a family owned and run company with coffee being in our blood, currently being run by 3rd gen coffee farmers with roots tying back to coffee growing in Tanzania. We grow, process and roast a very high quality Arabica Coffee (It has won the Gold/ The best milk based coffee in Australia at the silver kettle prizes in the past). We package our coffee beans and ground coffee into 1kg and 250gram bags, which are a bit dated now. We would love to get some amazing designs to bring our product into the future. Our target audience would be 25yrs- 60yr old with a large proportion coming to our plantation to do a tour enjoy a cup, take home a momento and then turn into an online customer.
Content
We would like to achieve a modern standout packaging design that reflects our premium quality Australian coffee. We have a medium roast and an espresso roast lines that we grow roast and sell.
We are happy to see designs that are creative and unique, not just another coffee bag on the shelf, but a standout premium product, that reflects that the coffee is actually grown in Australia, not just roasted here.
Our current colours are red and gold, and we are looking to package our coffee in box bottom bags with rippa zippas with both the 1kg and 250 gram lines, but are open to any other fantastic packaging concepts too.
The bag need to communicate the high quality of the bean within.
Some brainstormed keywords are: Australian, Fresh, Single Origin, Premium, Reserve, Cafe, Barista, Very High Quality, Grown, Plantation.

Target Market(s)

The target market is 25yrs+

Industry/Entity Type

It Company

Font styles to use
Sans Serif
Script

Colors
ec1f27
ffffff
ffc214
0792cd
9bcb3c

Requirements
Must have
• A unique design that stands out from all the rest, ie I'll buy this one! It is more expensive but the package looks so premium i don't mind paying extra for it.
• -Name of roast:(Espresso Roast, Beans), (Espresso Roast, Fine Grind), (Medium Roast beans), ( Medium roast, Plunger/Drip Grind).
• - An area on the back of the package for a barcode Ean13.
Nice to have
• Class added, either in a fancy emblem (think Australian nation emblem except better :)
• Something really attractive in the side gussets
• Clear and concise, uncluttered.
Should not have
• Just a picture of a kangaroo/ koala...

```html
<!DOCTYPE html>
<html lang="en">
<head>
<meta charset="utf-8">
<title>Morrell Coffee – Espresso Roast Bag Range</title>
<link href="https://fonts.googleapis.com/css2?family=Fira+Sans:wght@500;600&family=Montserrat:wght@500;600&family=Arimo:wght@700&display=swap" rel="stylesheet">
<style>
  :root {
    --stage: #0e0708;
    --red-body: #7a2622;
    --red-deep: #4a0c06;
    --gold-hi: #f1d35f;
    --gold-lo: #a9822e;
    --gold-text: #f0c850;
    --red-text: #9a2a20;
    --cream: #e8cfa6;
    --beige: #c8a878;
    --yellow: #f3e35a;
    --net-yellow: #ffe21a;
  }
  * { box-sizing: border-box; margin: 0; padding: 0; }
  html, body { width: 1200px; height: 739px; overflow: hidden; background: var(--stage); }
  .range { position: relative; width: 1200px; height: 739px; }

  .bag { position: absolute; width: 260px; height: 494px; overflow: hidden; }
  .bag--red { left: 128px; top: 122px; background: linear-gradient(90deg, #5e1a17 0%, var(--red-body) 15%, #852d27 55%, var(--red-body) 90%, #561814 100%); }
  .bag--gold { left: 480px; top: 124px; background: linear-gradient(90deg, #4c4222 0%, #8c7a38 20%, #d9b842 55%, #a08a3a 85%, #4a3f20 100%); }
  .bag--sand { left: 836px; top: 130px; background: linear-gradient(90deg, #8a6e48 0%, var(--beige) 20%, #dcc294 55%, var(--beige) 85%, #8c704a 100%); }

  .bag__pattern { position: absolute; left: 0; right: 0; top: 230px; bottom: 0; }
  .bag--red .bag__pattern { background: radial-gradient(ellipse at 70% 60%, rgba(90,15,10,.35), transparent 70%); }
  .bag--gold .bag__pattern { background: radial-gradient(ellipse at 60% 70%, rgba(60,30,10,.3), transparent 70%); }
  .bag--sand .bag__pattern { background: radial-gradient(ellipse at 60% 70%, rgba(90,40,20,.25), transparent 70%); }

  .bag__panel { position: absolute; left: 28px; top: 0; width: 202px; height: 226px;
    clip-path: polygon(0 0, 100% 0, 100% 86%, 50% 100%, 0 86%); }
  .bag--red .bag__panel { background: linear-gradient(135deg, var(--gold-hi) 0%, #d8b44a 45%, var(--gold-lo) 100%); }
  .bag--gold .bag__panel, .bag--sand .bag__panel { background: linear-gradient(180deg, #3e0904, var(--red-deep) 60%, #5a1208); }

  .line { position: absolute; left: 0; right: 0; text-align: center; }
  .origin { top: 44px; font: 600 10px/14px "Montserrat", sans-serif; letter-spacing: 1.5px; }
  .brand { top: 136px; font: 500 28px/30px "Fira Sans", sans-serif; letter-spacing: 1px; }
  .tagline { top: 170px; font: 600 14px/16px "Fira Sans", sans-serif; }
  .bag--red .origin, .bag--red .brand, .bag--red .tagline { color: var(--red-text); }
  .bag--gold .origin, .bag--gold .brand, .bag--gold .tagline,
  .bag--sand .origin, .bag--sand .brand, .bag--sand .tagline { color: var(--gold-text); }

  .seal { position: absolute; left: 98px; top: 238px; width: 64px; height: 64px; border-radius: 50%;
    border: 1.5px solid rgba(232,207,166,.75); }
  .bag--sand .seal { border-color: rgba(245,230,190,.85); }

  .grade { top: 318px; font: 600 9px/12px "Montserrat", sans-serif; letter-spacing: 2px; color: var(--cream); }
  .origin-type { top: 332px; font: 500 9px/12px "Montserrat", sans-serif; letter-spacing: 1.2px; color: var(--cream); }
  .roast { top: 347px; font: 600 25px/28px "Fira Sans", sans-serif; letter-spacing: 1.5px; color: var(--cream); }
  .grind { top: 377px; font: 600 17px/20px "Fira Sans", sans-serif; letter-spacing: .8px; color: var(--cream); }
  .bag--sand .grade, .bag--sand .origin-type { color: #f6ecc4; }
  .bag--sand .roast, .bag--sand .grind { color: var(--yellow); }
  .weight { top: 461px; font: 700 10px/12px "Arimo", sans-serif; color: var(--net-yellow); }
</style>
</head>
<body>
<main class="range">
  <section class="bag bag--red">
    <div class="bag__pattern" role="img" aria-label="Flowing topographic contour-line pattern in deep red"></div>
    <div class="bag__panel"></div>
    <p class="line origin">AUSTRALIAN GROWN<br>COFFEE</p>
    <p class="line brand">MORRELL</p>
    <p class="line tagline">AUSTRALIAN COFFEE</p>
    <div class="seal"></div>
    <p class="line grade">PREMUIM</p>
    <p class="line origin-type">SINGLE ORIGIN COFFEE</p>
    <p class="line roast">ESPRESSO ROAST</p>
    <p class="line grind">GROUND COFFEE</p>
    <p class="line weight">NET WEIGHT 500 OZ &nbsp;(1 Kg)</p>
  </section>

  <section class="bag bag--gold">
    <div class="bag__pattern" role="img" aria-label="Flowing topographic contour-line pattern in dark brown"></div>
    <div class="bag__panel"></div>
    <p class="line origin">AUSTRALIAN GROWN<br>COFFEE</p>
    <p class="line brand">MORRELL</p>
    <p class="line tagline">AUSTRALIAN COFFEE</p>
    <div class="seal"></div>
    <p class="line grade">PREMUIM</p>
    <p class="line origin-type">SINGLE ORIGIN COFFEE</p>
    <p class="line roast">ESPRESSO ROAST</p>
    <p class="line grind">GROUND COFFEE</p>
    <p class="line weight">NET WEIGHT 500 OZ &nbsp;(1 Kg)</p>
  </section>

  <section class="bag bag--sand">
    <div class="bag__pattern" role="img" aria-label="Flowing topographic contour-line pattern in brown"></div>
    <div class="bag__panel"></div>
    <p class="line origin">AUSTRALIAN GROWN<br>COFFEE</p>
    <p class="line brand">MORRELL</p>
    <p class="line tagline">AUSTRALIAN COFFEE</p>
    <div class="seal"></div>
    <p class="line grade">PREMUIM</p>
    <p class="line origin-type">SINGLE ORIGIN COFFEE</p>
    <p class="line roast">ESPRESSO ROAST</p>
    <p class="line grind">GROUND COFFEE</p>
    <p class="line weight">NET WEIGHT 500 OZ &nbsp;(1 Kg)</p>
  </section>
</main>
</body>
</html>
```